KM Talbot Transport needs a Business Card and Stationery

Hello, designers. Will appreciate your designs for a business card using the logo seen attached to this brief.

No particular preference in terms of design - design should have similar vision as logo. Website is www.kmtalbottransport-example.com

Winner of this business card design contest will automatically be invited to do 1on1 project for Stationery Design.

Business card will be printed for 3 or 4 persons, hence, will provide other names and details in the handover page once the winning design is selected.

Target Market(s)

We are a Transportation company (Buses) we offer transportation for large groups and small.

Industry/Entity Type

Business

Contact Information for Business Card

Marcella Talbot
KM Talbot Transport Inc.
58 Ostley Ave
Walpole, MA
02081
Toll Free Number 1-844-KMTALBT
www.kmtalbottransport-example.com
*email and contact number/s will be provided in the handover page after winner is chosen*

2nd or back page will show the services we offer: AND LOGO WITH GO SAFE GO IN STYLE
Weddings
Corporate
Airport Transportation
Casino Trips
Theme Parks
email quote@kmtalbottransport-example.com

```html
<!DOCTYPE html>
<html lang="en">
<head>
<meta charset="utf-8">
<title>KM Talbot Transport – Business Card</title>
<link rel="stylesheet" href="https://fonts.googleapis.com/css2?family=Open+Sans:ital,wght@0,400;0,600;0,700;1,400&family=Roboto+Condensed:ital,wght@1,700&display=swap">
<style>
  :root{
    --page:#ffffff;
    --ink:#2a2a2a;
    --muted:#555a60;
    --blue:#1f8fd6;
    --blue-deep:#0f6fb3;
    --blue-pale:#8cc4ea;
  }
  *{box-sizing:border-box;margin:0;padding:0}
  html,body{width:898px;height:1200px;overflow:hidden;background:var(--page)}
  body{position:relative;font-family:"Open Sans",Arial,sans-serif;color:var(--ink)}
  .side-label{position:absolute;left:6px;font-size:26px;color:#333}
  .side-label--front{top:6px}
  .side-label--back{top:600px}
  .card{position:absolute;left:36px;width:841px;height:519px;overflow:hidden;box-shadow:0 0 0 1px #c9c9c9}
  .card--front{top:62px}
  .card--back{top:652px}
  .card-bg{position:absolute;inset:0;width:100%;height:100%}
  .company-name{position:absolute;left:60px;top:62px;font-size:44px;font-weight:700;color:var(--blue-deep);line-height:1.05;width:420px}
  .holder-name{position:absolute;left:54px;top:268px;font-size:31px;font-weight:600;color:var(--ink);display:flex;align-items:center;gap:16px}
  .holder-name::after{content:"";width:64px;height:2px;background:var(--muted)}
  .company-legal{position:absolute;left:54px;top:372px;font-size:19px;letter-spacing:6px;color:var(--muted);text-transform:uppercase}
  .contact-col{position:absolute;top:414px;font-size:16px;line-height:28px;color:var(--ink)}
  .contact-col::before{content:"";display:block;width:72px;height:3px;background:var(--blue);margin-bottom:6px}
  .contact-col--address{left:54px}
  .contact-col--mail{left:279px}
  .contact-col--web{left:522px}
  .contact-col .key{color:var(--blue)}
  .toll-free{display:inline-block;background:var(--blue-deep);color:#fff;padding:0 8px;margin-left:6px;line-height:24px}
  .tagline-head{position:absolute;left:159px;top:48px;font-family:"Roboto Condensed",Arial,sans-serif;font-style:italic;font-weight:700;font-size:35px;color:#222;letter-spacing:.3px}
  .tagline-sub{position:absolute;right:142px;top:94px;font-size:18px;font-style:italic;color:var(--blue)}
  .services{position:absolute;left:54px;top:212px;display:grid;grid-template-columns:330px 300px;row-gap:20px;list-style:none}
  .service{display:flex;align-items:center;gap:16px;font-size:24px;color:#222;font-weight:600}
  .tick{width:28px;height:28px;flex:none}
  .quote-mail{position:absolute;left:54px;top:424px;font-size:18px;color:var(--ink)}
  .quote-mail::before{content:"";display:block;width:72px;height:3px;background:var(--blue);margin-bottom:14px}
  .quote-mail .key{color:var(--blue)}
  .back-web{position:absolute;right:22px;top:456px;font-size:15px;color:#fff}
</style>
</head>
<body>
  <div class="side-label side-label--front">Front</div>

  <section class="card card--front" aria-label="Business card front">
    <svg class="card-bg" viewBox="0 0 841 519" preserveAspectRatio="none" aria-hidden="true">
      <defs>
        <linearGradient id="frontLight" x1="0" y1="0" x2="1" y2="1">
          <stop offset="0" stop-color="#f7f7f7"/><stop offset="1" stop-color="#d9dadc"/>
        </linearGradient>
        <linearGradient id="frontDark" x1="0" y1="0" x2="1" y2="1">
          <stop offset="0" stop-color="#6b6e72"/><stop offset=".5" stop-color="#3a3c40"/><stop offset="1" stop-color="#1f2023"/>
        </linearGradient>
      </defs>
      <rect width="841" height="519" fill="url(#frontLight)"/>
      <path d="M560 0 C610 150 700 290 841 370 L841 0 Z" fill="url(#frontDark)"/>
      <path d="M545 0 C600 160 700 300 841 390" fill="none" stroke="#1f8fd6" stroke-width="16"/>
      <path d="M520 0 C585 175 690 320 841 415" fill="none" stroke="#8cc4ea" stroke-width="3"/>
    </svg>

    <div class="company-name">KM Talbot Transport</div>
    <h1 class="holder-name">Marcella Talbot</h1>
    <div class="company-legal">KM Talbot Transport Inc.</div>

    <div class="contact-col contact-col--address">
      <div><span class="key">A:</span> 58 Ostley Ave</div>
      <div>&nbsp;&nbsp;&nbsp;Harlow, NH 03104</div>
    </div>
    <div class="contact-col contact-col--mail">
      <div><span class="key">E:</span> youremail@web.com</div>
      <div><span class="key">P:</span> 0123 456 7890</div>
    </div>
    <div class="contact-col contact-col--web">
      <div><span class="key">W:</span> www.kmtalbottransport-example.com</div>
      <div><span class="key">Toll Free</span><span class="toll-free">1 (844) KM TALBT</span></div>
    </div>
  </section>

  <div class="side-label side-label--back">Back</div>

  <section class="card card--back" aria-label="Business card back">
    <svg class="card-bg" viewBox="0 0 841 519" preserveAspectRatio="none" aria-hidden="true">
      <defs>
        <linearGradient id="backLight" x1="0" y1="0" x2="1" y2="1">
          <stop offset="0" stop-color="#f6f6f6"/><stop offset="1" stop-color="#dadbdd"/>
        </linearGradient>
        <linearGradient id="backDark" x1="0" y1="0" x2="1" y2="1">
          <stop offset="0" stop-color="#9a9da1"/><stop offset="1" stop-color="#3b3d41"/>
        </linearGradient>
        <linearGradient id="backCorner" x1="0" y1="0" x2="1" y2="1">
          <stop offset="0" stop-color="#4a4d51"/><stop offset="1" stop-color="#1e1f22"/>
        </linearGradient>
      </defs>
      <rect width="841" height="519" fill="url(#backLight)"/>
      <path d="M470 0 L841 0 L841 280 C760 160 640 60 470 0 Z" fill="url(#backDark)" opacity=".7"/>
      <path d="M420 519 C560 420 720 350 841 320 L841 519 Z" fill="url(#backCorner)"/>
      <path d="M405 519 C548 408 712 336 841 305" fill="none" stroke="#1f8fd6" stroke-width="16"/>
      <path d="M382 519 C530 392 700 318 841 284" fill="none" stroke="#8cc4ea" stroke-width="3"/>
    </svg>

    <h2 class="tagline-head">WHEN IN NEED OF TRANSPORTATION</h2>
    <div class="tagline-sub">Go safe go in style!</div>

    <ul class="services">
      <li class="service"><svg class="tick" viewBox="0 0 28 28" aria-hidden="true"><rect width="28" height="28" fill="var(--blue)"/><path d="M6 14 L12 20 L22 8" fill="none" stroke="#fff" stroke-width="3.5"/></svg>Weddings</li>
      <li class="service"><svg class="tick" viewBox="0 0 28 28" aria-hidden="true"><rect width="28" height="28" fill="var(--blue)"/><path d="M6 14 L12 20 L22 8" fill="none" stroke="#fff" stroke-width="3.5"/></svg>Casino Trips</li>
      <li class="service"><svg class="tick" viewBox="0 0 28 28" aria-hidden="true"><rect width="28" height="28" fill="var(--blue)"/><path d="M6 14 L12 20 L22 8" fill="none" stroke="#fff" stroke-width="3.5"/></svg>Corporate</li>
      <li class="service"><svg class="tick" viewBox="0 0 28 28" aria-hidden="true"><rect width="28" height="28" fill="var(--blue)"/><path d="M6 14 L12 20 L22 8" fill="none" stroke="#fff" stroke-width="3.5"/></svg>Theme Parks</li>
      <li class="service"><svg class="tick" viewBox="0 0 28 28" aria-hidden="true"><rect width="28" height="28" fill="var(--blue)"/><path d="M6 14 L12 20 L22 8" fill="none" stroke="#fff" stroke-width="3.5"/></svg>Airport Transportation</li>
    </ul>

    <div class="quote-mail"><span class="key">E:</span> quote@kmtalbottransport-example.com</div>
    <div class="back-web">www.KMTalbotTransport-example.com</div>
  </section>
</body>
</html>
```